Square Business Cards for Our Restaurant / Event Venue

We need square business cards designed for the management team of our event venue and restaurant. On one side of the card should be the the Harbor Lantern 7 logo and URL www.harborlantern7.example. On the other side should be the Ember Logo and URL www.emberhall7.example. All employee details should be on the side with Ember logo. There will be a total of 5 cards to be created with the design.

Clara Bennquist
clara@harborlantern7.example

main 555.418.3072
direct 555.730.2946

4831 West Orchard Lane SE
Washington, DC 90417

Industry/Entity Type

Business

```html
<!DOCTYPE html>
<html lang="en">
<head>
<meta charset="utf-8">
<title>Ember / Harbor Lantern 7 – Square Business Cards</title>
<link rel="stylesheet" href="https://fonts.googleapis.com/css2?family=Oswald:wght@600&family=Roboto:wght@400;700&display=swap">
<style>
  :root {
    --backdrop-top: #b9c0c6;
    --backdrop-bottom: #e6eaed;
    --paper: #f1f1f0;
    --ink: #1d1d1d;
    --brand-red: #a8161c;
    --band-black: #0c0c0c;
  }
  * { box-sizing: border-box; margin: 0; padding: 0; }
  html, body { width: 1200px; height: 1200px; overflow: hidden; }
  body {
    background: linear-gradient(180deg, var(--backdrop-top), var(--backdrop-bottom) 45%, var(--backdrop-bottom));
    font-family: "Roboto", Arial, sans-serif;
    color: var(--ink);
    display: flex;
    align-items: center;
    justify-content: center;
    gap: 60px;
  }
  .card {
    position: relative;
    width: 500px;
    height: 500px;
    background: var(--paper);
    border-radius: 44px;
    overflow: hidden;
    box-shadow: 0 10px 24px rgba(40, 50, 60, 0.22);
  }

  /* Front: personal details */
  .card-front {
    display: flex;
    flex-direction: column;
    align-items: center;
    text-align: center;
    padding-top: 62px;
  }
  .brand-name {
    font-family: "Roboto", Arial, sans-serif;
    font-weight: 700;
    font-size: 74px;
    line-height: 1;
    color: var(--ink);
    letter-spacing: 1px;
  }
  .person-name {
    margin-top: 26px;
    font-family: "Oswald", "Arial Narrow", sans-serif;
    font-weight: 600;
    font-size: 30px;
    letter-spacing: 0.5px;
    text-transform: uppercase;
    color: var(--brand-red);
    padding: 0 16px 4px;
    border-bottom: 2px solid var(--brand-red);
  }
  .contact {
    margin-top: 10px;
    font-size: 17px;
    line-height: 1.3;
  }
  .contact .spaced { margin-top: 12px; }
  .phones {
    margin-top: 10px;
    font-size: 19px;
    line-height: 1.3;
  }
  .phones .label { color: var(--brand-red); font-weight: 700; }
  .bottom-bands {
    position: absolute;
    left: 0; right: 0; bottom: 0;
  }
  .bottom-bands .red-stripe { height: 7px; background: var(--brand-red); }
  .bottom-bands .gap { height: 6px; }
  .bottom-bands .black-band { height: 44px; background: var(--band-black); }

  /* Back: venue mark */
  .card-back {
    display: flex;
    flex-direction: column;
    align-items: center;
  }
  .venue-mark {
    margin-top: 108px;
    display: flex;
    align-items: center;
    gap: 16px;
  }
  .venue-dot {
    width: 40px; height: 40px;
    border-radius: 50%;
    background: var(--brand-red);
  }
  .venue-name {
    font-family: "Roboto", Arial, sans-serif;
    font-weight: 700;
    font-size: 42px;
    color: var(--brand-red);
  }
  .venue-url {
    margin-top: auto;
    margin-bottom: 62px;
    font-size: 17px;
  }
  .venue-url .accent { color: var(--brand-red); }
</style>
</head>
<body>
  <section class="card card-front">
    <div class="brand-name">Ember</div>
    <div class="person-name">Clara Bennquist</div>
    <div class="contact">
      <div>4831 West Orchard Lane SE</div>
      <div>Washington, DC 90417</div>
      <div class="spaced">www.emberhall7.example</div>
      <div>clara@harborlantern7.example</div>
    </div>
    <div class="phones">
      <div><span class="label">Main:</span> 555.418.3072</div>
      <div><span class="label">Direct:</span> 555.730.2946</div>
    </div>
    <div class="bottom-bands">
      <div class="red-stripe"></div>
      <div class="gap"></div>
      <div class="black-band"></div>
    </div>
  </section>

  <section class="card card-back">
    <div class="venue-mark">
      <span class="venue-dot"></span>
      <span class="venue-name">Harbor Lantern 7</span>
    </div>
    <div class="venue-url">www.<span class="accent">harborlantern7.example</span></div>
  </section>
</body>
</html>
```